Marrowfield Biomedical Research Institute (MBRX) Web Design

MBRX is a non-profit organization focused on saving the lives of terminally ill patients by becoming the leaders in cutting-edge research, innovative technologies, utilizing national and international partnerships as well as the associated allopathic and naturopathic treatments necessary to do so.

Our primary focus is raising funds to support the research and acquisition of new technologies for life saving treatments which are NOT a one size fits all approach like conventional medicine but rather a marriage of the latest technologies used in combination with other new treatment possibilities for a successful end result.

Our domain is marrowfieldbrx.org

Logo files are attached.

Looking for something clean, light, healthy.

Target Market(s)

The site should look and feel towards research/scientific grant writing.
Medical professionals, Medical Scientists.

Industry/Entity Type

Medical And Science

Number of Pages Required

4 page

Requirements
Nice to have
• Here are examples of sites I like in the order of how much I like them.
• https://www.palvenhope.org/give.html
• https://www.thekqtf.org/donate-to-kqtf
• https://www.velmorecure.org/we-are-vci/join-the-cause
• https://www.tumarex.org/involved/donate.html
• https://give.dwkt.org/checkout/donation?eid=58217
• https://www.quillavent.org/how-you-can-help
• https://donate3.tumarex.org/

```html
<!DOCTYPE html>
<html lang="en">
<head>
<meta charset="utf-8">
<title>Marrowfield – Biomedical Research Institute</title>
<link href="https://fonts.googleapis.com/css2?family=Poppins:wght@400;500;600;700&family=Open+Sans:wght@400;600&display=swap" rel="stylesheet">
<style>
:root{
  --green:#7cc242;
  --green-dark:#6aae33;
  --blue:#1a7fc8;
  --blue-deep:#136bb0;
  --ink:#222831;
  --text:#555b63;
  --muted:#9aa0a6;
  --line:#e6e8ea;
  --soft:#f4f5f6;
  --footer:#1f232a;
  --white:#fff;
}
*{box-sizing:border-box;margin:0;padding:0}
html,body{width:1200px;height:3782px;overflow:hidden}
body{font-family:"Open Sans",Arial,sans-serif;color:var(--text);background:var(--white);position:relative}
h1,h2,h3,h4,.btn,.nav a{font-family:Poppins,Arial,sans-serif}
.abs{position:absolute}
a{text-decoration:none;color:inherit}

.topbar{top:0;left:0;width:1200px;height:35px;border-bottom:1px solid var(--line);font-size:11px;color:#777;display:flex;align-items:center;justify-content:space-between;padding:0 88px}
.topbar .right{display:flex;gap:30px;align-items:center}
.topbar .right span{display:flex;align-items:center;gap:7px}
.dot{width:12px;height:12px;border-radius:50%;background:#c9ccd0;display:inline-block}
.dot.flag{background:#3a5aa8}

.brand{top:66px;left:88px;display:flex;align-items:center;gap:12px}
.brand .mark{width:26px;height:26px;background:var(--green)}
.brand .name{font-family:Poppins,sans-serif;font-weight:500;font-size:27px;color:var(--ink)}
.search{top:68px;left:640px;width:322px;height:40px;border:1px solid var(--line);border-radius:3px;font-size:11px;color:var(--muted);padding:0 14px;display:flex;align-items:center;justify-content:space-between}
.btn{display:inline-flex;align-items:center;justify-content:center;font-size:12px;font-weight:600;letter-spacing:.5px;text-transform:uppercase}
.btn-green{background:var(--green);color:var(--white);border-radius:3px}
.header-donate{top:68px;left:985px;width:125px;height:40px}
.nav{top:140px;left:0;width:1200px;height:42px;border-bottom:1px solid var(--line);border-top:1px solid var(--line)}
.nav a{position:absolute;top:13px;font-size:11px;font-weight:500;text-transform:uppercase;color:#444}
.nav a.active{color:var(--green)}
.nav a.active::after{content:"";position:absolute;left:0;right:0;top:24px;height:3px;background:var(--green)}

.hero{top:182px;left:0;width:1200px;height:569px;background:linear-gradient(120deg,#4a3a2c 0%,#7b6650 45%,#9b8a78 70%,#5d4c3d 100%)}
.hero-kicker{top:385px;left:88px;color:var(--white);font-family:Poppins,sans-serif;font-size:22px;font-weight:500}
.hero-title{top:410px;left:88px;color:var(--white);font-size:58px;font-weight:700}
.btn-white{background:var(--white);color:var(--ink);border-radius:2px}
.hero-btn{top:497px;left:88px;width:142px;height:42px;font-size:11px}
.hero-arrow{top:440px;width:42px;height:52px;background:var(--white);display:flex;align-items:center;justify-content:center}
.scroll{top:672px;left:550px;width:100px;text-align:center;color:var(--white);font-size:9px;font-weight:600;letter-spacing:.5px}
.scroll .mouse{width:18px;height:30px;border:2px solid var(--white);border-radius:9px;margin:8px auto 0}

.about-photo{top:872px;left:103px;width:434px;height:335px;background:linear-gradient(135deg,#6f6256,#a59886 50%,#4f463e)}
.eyebrow{font-family:Poppins,sans-serif;font-size:12px;font-weight:600;letter-spacing:2px;color:var(--blue)}
.about-text{top:860px;left:620px;width:492px}
.about-text h2{font-size:28px;font-weight:500;color:var(--ink);line-height:1.15;margin:8px 0 36px}
.about-text p{font-size:13px;line-height:1.85;margin-bottom:18px}
.btn-outline{border:2px solid var(--ink);color:var(--ink);height:44px;width:195px;font-size:10.5px;margin-top:12px}

.topics{top:1311px;left:0;width:1200px;height:668px;background:var(--soft)}
.section-title{left:0;width:1200px;text-align:center;font-size:27px;font-weight:500;color:var(--ink)}
.section-title.light{color:var(--white)}
.section-title::after{content:"";display:block;width:36px;height:2px;background:currentColor;margin:18px auto 0;opacity:.8}
.pager{display:flex;gap:14px}
.card{width:323px;background:var(--white);box-shadow:0 4px 16px rgba(0,0,0,.06)}
.card .ph{height:218px}
.card .body{padding:24px 26px}
.card h3{font-size:17px;font-weight:500;color:var(--ink);margin-bottom:8px}
.card p{font-size:11.5px;line-height:1.6}
.more{display:flex;align-items:center;gap:10px;margin-top:22px;font-size:10px;font-weight:600;color:#c4c8cc;text-transform:uppercase;font-family:Poppins,sans-serif}
.more.on{color:var(--green)}
.more .c{width:20px;height:20px;border-radius:50%;border:1px solid currentColor;display:flex;align-items:center;justify-content:center}
.more.on .c{background:var(--green);border-color:var(--green)}

.donate{top:1979px;left:0;width:1200px;height:504px;background:linear-gradient(90deg,var(--blue-deep),var(--blue) 55%,#2a8ed4)}
.way{top:2180px;width:260px;text-align:center;color:var(--white)}
.way .icon{width:106px;height:106px;border-radius:50%;background:var(--white);margin:0 auto 20px;display:flex;align-items:center;justify-content:center}
.way .icon.active{background:var(--green);box-shadow:0 0 0 5px rgba(255,255,255,.35)}
.way h4{font-size:15px;font-weight:500;line-height:1.45}
.chev{width:22px;height:22px;border-radius:50%;background:var(--white);margin:10px auto 0;display:flex;align-items:center;justify-content:center}

.news-card{top:2657px;background:var(--white);box-shadow:0 6px 20px rgba(0,0,0,.08);height:418px}
.news-card .meta{font-size:11px;color:#666;margin-bottom:16px}
.news-card h3{font-size:17px;font-weight:500;color:var(--ink);line-height:1.55}
.news-card p{font-size:11.5px;line-height:1.75;margin-top:20px}

.contact{top:3164px;left:0;width:1200px;height:169px;background:var(--green);color:var(--white)}
.contact h2{position:absolute;top:48px;left:88px;font-size:26px;font-weight:500;line-height:1.3}
.cinfo{position:absolute;top:58px;display:flex;gap:16px;align-items:flex-start}
.cinfo .ic{width:40px;height:40px;border-radius:50%;background:rgba(255,255,255,.22);display:flex;align-items:center;justify-content:center;margin-top:2px}
.cinfo b{display:block;font-family:Poppins,sans-serif;font-weight:400;font-size:19px}
.cinfo span{font-size:12px}
.contact .btn{position:absolute;top:58px;left:987px;width:124px;height:48px;font-size:11px;box-shadow:0 3px 10px rgba(0,0,0,.15)}

.footer{top:3333px;left:0;width:1200px;height:449px;background:var(--footer);color:#b8bcc2}
.fcol{position:absolute;top:68px}
.fcol h4{font-size:14px;font-weight:500;color:var(--white);margin-bottom:20px}
.fcol li{list-style:none;font-size:12px;line-height:40px}
.fcol li::before{content:"› ";color:#888}
.social{display:flex;gap:10px;margin-bottom:36px}
.social i{width:32px;height:32px;border-radius:50%;display:block}
.mail{width:256px;height:40px;background:var(--white);border-radius:2px;display:flex;align-items:center;justify-content:space-between;padding:0 14px;font-size:11px;color:var(--muted)}
.copy{position:absolute;top:400px;left:0;width:1200px;border-top:1px solid #30353d;padding-top:18px;text-align:center;font-size:11px;color:var(--white)}
.totop{top:3728px;left:1136px;width:40px;height:40px;border-radius:50%;background:var(--blue);display:flex;align-items:center;justify-content:center}
</style>
</head>
<body>

<div class="abs topbar">
  <span>MBRX Marrowfield Biomedical Research Institute</span>
  <div class="right">
    <span><i class="dot"></i>LIVE CHAT</span>
    <span><i class="dot flag"></i>ENGLISH ▾</span>
    <span><i class="dot"></i>LOGIN</span>
  </div>
</div>

<div class="abs brand"><span class="mark"></span><span class="name">Marrowfield</span></div>
<div class="abs search">Search here...
  <svg width="14" height="14" viewBox="0 0 14 14"><circle cx="6" cy="6" r="4.5" fill="none" stroke="#999" stroke-width="1.4"/><line x1="9.5" y1="9.5" x2="13" y2="13" stroke="#999" stroke-width="1.4"/></svg>
</div>
<a class="abs btn btn-green header-donate">Donate Now</a>

<nav class="abs nav">
  <a class="active" style="left:88px">Home</a>
  <a style="left:155px">About Us</a>
  <a style="left:245px">Care &amp; Treatment</a>
  <a style="left:385px">Research</a>
  <a style="left:480px">Training</a>
  <a style="left:565px">Get Involved</a>
  <a style="left:672px">Ways to Give</a>
  <a style="left:790px">Contact Us</a>
</nav>

<div class="abs hero" role="img" aria-label="Photo of a young child sitting on a wooden deck outdoors"></div>
<div class="abs hero-kicker">MBRX is a Non-Profit Organization On</div>
<h1 class="abs hero-title">Saving The Lives</h1>
<a class="abs btn btn-white hero-btn">Get Involved</a>
<div class="abs hero-arrow" style="left:0;width:22px"><svg width="8" height="12" viewBox="0 0 8 12"><path d="M6 1 1 6l5 5" fill="none" stroke="#333" stroke-width="1.6"/></svg></div>
<div class="abs hero-arrow" style="left:1158px"><svg width="8" height="12" viewBox="0 0 8 12"><path d="M2 1l5 5-5 5" fill="none" stroke="#333" stroke-width="1.6"/></svg></div>
<div class="abs scroll">SCROLL DOWN<div class="mouse"></div></div>

<div class="abs about-photo" role="img" aria-label="Photo of two young children walking together on a stone path"></div>
<div class="abs about-text">
  <div class="eyebrow">ABOUT US</div>
  <h2>Some short introduction<br>about the company</h2>
  <p>Aenean sollicitudin, lorem quis bibendum auctor, nisi elit consequat ipsum, nec sagittis sem nibh id elit. Duis sed odio sit amet nibh vulputate cursus a sit amet mauris. Morbi accumsan ipsum velit nam nec tellus a odio tincidunt auctor a ornare odio.</p>
  <p>Sed non mauris vitae erat consequat auctor eu in elit. Class aptent taciti ad litora torquent per conubia nostra, per inceptos himenaeos.</p>
  <a class="btn btn-outline">Learn More About Us</a>
</div>

<section class="abs topics"></section>
<h2 class="abs section-title" style="top:1410px">More Topics In Treatment &amp; Suport</h2>
<div class="abs pager" style="top:1420px;left:1040px">
  <svg width="26" height="12" viewBox="0 0 26 12"><path d="M25 6H2M7 1 2 6l5 5" fill="none" stroke="#cfd3d6" stroke-width="1.4"/></svg>
  <svg width="26" height="12" viewBox="0 0 26 12"><path d="M1 6h23M19 1l5 5-5 5" fill="none" stroke="#7cc242" stroke-width="1.4"/></svg>
</div>
<div class="abs card" style="top:1502px;left:88px">
  <div class="ph" role="img" aria-label="Photo of a nurse assisting a patient in a wheelchair" style="background:linear-gradient(135deg,#d8cbb8,#b9a893 60%,#e9e1d6)"></div>
  <div class="body"><h3>During &amp; After Treatment</h3><p>Sed non mauris vitae erat consequat auctor eu in elit class aptent taciti ad litora</p>
  <div class="more"><span class="c"><svg width="6" height="8"><path d="M1 1l4 3-4 3" fill="none" stroke="#c4c8cc" stroke-width="1.2"/></svg></span>View Details</div></div>
</div>
<div class="abs card" style="top:1502px;left:438px">
  <div class="ph" role="img" aria-label="Photo of a hand holding a blood glucose meter" style="background:linear-gradient(135deg,#e4e7ea,#c7ccd2 55%,#f1f2f3)"></div>
  <div class="body"><h3>Clinic Trials</h3><p>Sed non mauris vitae erat consequat auctor eu in elit class aptent taciti ad litora</p>
  <div class="more on"><span class="c"><svg width="6" height="8"><path d="M1 1l4 3-4 3" fill="none" stroke="#fff" stroke-width="1.2"/></svg></span>View Details</div></div>
</div>
<div class="abs card" style="top:1502px;left:788px">
  <div class="ph" role="img" aria-label="Photo of a man standing on a grassy green hillside" style="background:linear-gradient(160deg,#e9efe0,#8fb352 45%,#5f8a2a)"></div>
  <div class="body"><h3>Support In your Area</h3><p>Sed non mauris vitae erat consequat auctor eu in elit class aptent taciti ad litora</p>
  <div class="more"><span class="c"><svg width="6" height="8"><path d="M1 1l4 3-4 3" fill="none" stroke="#c4c8cc" stroke-width="1.2"/></svg></span>View Details</div></div>
</div>

<section class="abs donate" role="img" aria-label="Faint blue-toned photo of a child as background"></section>
<h2 class="abs section-title light" style="top:2078px">Way's To Donate Now!</h2>
<div class="abs pager" style="top:2088px;left:1036px">
  <svg width="26" height="12" viewBox="0 0 26 12"><path d="M25 6H2M7 1 2 6l5 5" fill="none" stroke="#fff" stroke-width="1.4"/></svg>
  <svg width="26" height="12" viewBox="0 0 26 12"><path d="M1 6h23M19 1l5 5-5 5" fill="none" stroke="#a6dd7b" stroke-width="1.4"/></svg>
</div>
<div class="abs way" style="left:55px">
  <div class="icon"><svg width="44" height="44" viewBox="0 0 44 44" fill="none" stroke="#222" stroke-width="2"><circle cx="26" cy="15" r="9"/><path d="M26 10v10M23 12h5M23 18h5"/><path d="M4 32l8-6h10l4 3-6 2"/><path d="M10 38l6-4h10l12-9"/></svg></div>
  <h4>Make a one-Time<br>Donation</h4>
</div>
<div class="abs way" style="left:330px">
  <div class="icon active"><svg width="48" height="48" viewBox="0 0 48 48" fill="none" stroke="#fff" stroke-width="2"><path d="M10 24a14 14 0 0 1 24-10M38 24a14 14 0 0 1-24 10"/><path d="M34 8v6h-6M14 40v-6h6"/><path d="M24 16v16M20 19h6a2.5 2.5 0 0 1 0 5h-4a2.5 2.5 0 0 0 0 5h6"/></svg></div>
  <h4>Set Up Recurring<br>Donation</h4>
  <div class="chev"><svg width="7" height="10"><path d="M1 1l4 4-4 4" fill="none" stroke="#1a7fc8" stroke-width="1.6"/></svg></div>
</div>
<div class="abs way" style="left:618px">
  <div class="icon"><svg width="46" height="46" viewBox="0 0 46 46" fill="none" stroke="#222" stroke-width="2"><path d="M23 30s-10-6-10-13a5 5 0 0 1 10-2 5 5 0 0 1 10 2c0 7-10 13-10 13z"/><path d="M4 24l7 10h8M42 24l-7 10h-8"/></svg></div>
  <h4>Give a Gift In Honor Or<br>Memory</h4>
</div>
<div class="abs way" style="left:910px">
  <div class="icon"><svg width="46" height="46" viewBox="0 0 46 46" fill="none" stroke="#222" stroke-width="2"><circle cx="23" cy="15" r="9"/><path d="M23 10v10M20 12h5M20 18h5"/><path d="M4 28l8 10h10M42 28l-8 10H24"/></svg></div>
  <h4>MBRX Donate To a<br>Fundraiser</h4>
</div>

<h2 class="abs section-title" style="top:2560px;font-size:26px">News Articles and Blog</h2>
<div class="abs news-card" style="left:88px;width:323px">
  <div role="img" aria-label="Photo of two young children in a dark forest" style="height:228px;background:linear-gradient(150deg,#2f3b45,#4f6573 50%,#243039)"></div>
  <div style="padding:32px 26px 0">
    <div class="meta">by Harlow D- 17 hours ago</div>
    <h3>News heading: Some news heading goes here...</h3>
    <div class="more on" style="margin-top:24px"><span class="c"><svg width="6" height="8"><path d="M1 1l4 3-4 3" fill="none" stroke="#fff" stroke-width="1.2"/></svg></span>Learn More News</div>
  </div>
</div>
<div class="abs news-card" style="left:443px;width:668px">
  <div style="position:absolute;left:28px;top:26px;width:290px">
    <div style="font-family:Poppins,sans-serif;font-size:19px;color:var(--ink);margin-bottom:60px">18 July</div>
    <div class="meta">by Admin I- 2 hours ago</div>
    <h3>Upcoming Event: Some event heading goes here with some description below.</h3>
    <p>Maecenas nec odio et ante tincidunt tempus donec vitae sapien ut libero venenatis faucibus nullam quis ante.</p>
    <div class="more on"><span class="c"><svg width="6" height="8"><path d="M1 1l4 3-4 3" fill="none" stroke="#fff" stroke-width="1.2"/></svg></span>Learn More Events</div>
  </div>
  <div role="img" aria-label="Photo of a family walking along a path at sunset" style="position:absolute;right:0;top:0;width:335px;height:418px;background:linear-gradient(180deg,#c9b9a6,#8a7a68 55%,#5a4c3f)"></div>
</div>

<section class="abs contact">
  <h2>Contact us Now<br>For Further Information.</h2>
  <div class="cinfo" style="left:488px"><span class="ic"><svg width="16" height="12" viewBox="0 0 16 12" fill="none" stroke="#fff" stroke-width="1.3"><rect x="1" y="1" width="14" height="10"/><path d="M1 1l7 6 7-6"/></svg></span><div><b>Email address:</b><span>info@example.com</span></div></div>
  <div class="cinfo" style="left:722px"><span class="ic"><svg width="14" height="14" viewBox="0 0 14 14"><path d="M3 1l2.5 3-1.5 1.5a8 8 0 0 0 4.5 4.5L10 8.5l3 2.5-1.5 2C6 13 1 8 1 2.5z" fill="#fff"/></svg></span><div><b>Phone number:</b><span>123 456 7890</span></div></div>
  <a class="btn btn-white">Donate Online</a>
</section>

<footer class="abs footer">
  <div class="fcol" style="left:88px"><h4>Quick Links</h4><ul><li>Care &amp; Treatment</li><li>Research</li><li>Training</li><li>Get involved</li><li>Ways to give</li><li>Contact us</li></ul></div>
  <div class="fcol" style="left:327px"><h4>Help &amp; Support</h4><ul><li>News &amp; Press</li><li>Multiple Knowledge Center</li><li>Privacy Policy</li><li>Donor Privacy Policy</li><li>Terms of Use</li></ul></div>
  <div class="fcol" style="left:600px"><h4>Stay Informed</h4><ul><li>Blog</li><li>News &amp; Publications</li><li>Event Calendar</li><li>Pressroom</li><li>Stories</li><li>Join The Causes</li></ul></div>
  <div class="fcol" style="left:855px"><h4>Stay Connected</h4>
    <div class="social"><i style="background:#3b5998"></i><i style="background:#1da1f2"></i><i style="background:#dd4b39"></i><i style="background:#0e76a8"></i><i style="background:#c13584"></i></div>
    <h4>Join our mailing list</h4>
    <div class="mail"><span>✉&nbsp; Enter email address</span><svg width="16" height="16" viewBox="0 0 16 16"><path d="M1 7l14-6-5 14-2-6z" fill="#1a7fc8"/></svg></div>
  </div>
  <div class="copy">Copyright © 2017 &nbsp;|&nbsp; All Rights Reserved</div>
</footer>
<div class="abs totop"><svg width="12" height="8" viewBox="0 0 12 8"><path d="M1 7l5-5 5 5" fill="none" stroke="#fff" stroke-width="1.6"/></svg></div>

</body>
</html>
```